Bright Oak Fitness Facility Business Cards

Business Card Design that incorporates the logo and tagline

Target Market(s)

Fitness, People Who Exercise

Contact Information for Business Card

2817 Mossgrove Bend Road
Tavares, Florida 32190
Phone: 352-555-Jump (5867)
www.brightoakfitness.example
info@brightoakfitness.example

Requirements
Must have
• Logo, Address, Website, email and tagline "More Than A Gym". Colors should be red/black/grey/white

```html
<!DOCTYPE html>
<html lang="en">
<head>
<meta charset="utf-8">
<title>Bright Oak Fitness Business Cards</title>
<link rel="stylesheet" href="https://fonts.googleapis.com/css2?family=Open+Sans:wght@400;600;700;800&display=swap">
<style>
  :root {
    --backdrop: #1c1c1d;
    --silver-light: #f2f2f2;
    --silver-mid: #d9d9da;
    --silver-dark: #bdbdbf;
    --brand-red: #ec1c24;
    --ink-black: #111111;
    --paper-white: #ffffff;
  }
  * { box-sizing: border-box; margin: 0; padding: 0; }
  html, body {
    width: 1200px; height: 960px; overflow: hidden;
    background: var(--backdrop);
    font-family: "Open Sans", Arial, sans-serif;
  }
  .canvas {
    width: 1200px; height: 960px;
    display: flex; flex-direction: column; align-items: center; justify-content: center;
    gap: 56px;
  }
  .card {
    position: relative; width: 700px; height: 400px; overflow: hidden;
    background:
      repeating-linear-gradient(0deg, rgba(255,255,255,0.18) 0 1px, rgba(0,0,0,0.03) 1px 3px),
      linear-gradient(120deg, var(--silver-dark) 0%, var(--silver-light) 45%, var(--silver-mid) 100%);
    box-shadow: 0 18px 40px rgba(0,0,0,0.55);
  }
  /* Front */
  .card-front { display: flex; flex-direction: column; align-items: center; justify-content: center; gap: 26px; }
  .brand-name {
    color: var(--brand-red); font-weight: 800; text-transform: uppercase; letter-spacing: 1px;
  }
  .card-front .brand-name { font-size: 52px; }
  .tagline {
    color: var(--brand-red); font-weight: 700; font-size: 20px; letter-spacing: 1px; text-transform: uppercase;
  }
  /* Back */
  .back-shapes { position: absolute; inset: 0; }
  .card-back .brand-name {
    position: absolute; top: 30px; left: 0; right: 0; text-align: center; font-size: 38px;
  }
  .social-list {
    position: absolute; top: 100px; left: 40px; right: 40px;
    display: flex; justify-content: space-between; list-style: none;
  }
  .social-item { display: flex; align-items: center; gap: 7px; font-size: 15px; color: var(--ink-black); }
  .social-dot { width: 12px; height: 12px; border: 1.5px solid var(--brand-red); border-radius: 50%; }
  .person {
    position: absolute; left: 24px; top: 200px; color: var(--paper-white); font-size: 15px; line-height: 1.45;
  }
  .person-name { font-weight: 800; font-size: 18px; text-transform: uppercase; }
  .contact-list {
    position: absolute; right: 24px; bottom: 30px; list-style: none;
    color: var(--paper-white); font-size: 16px; text-align: right;
  }
  .contact-list li { display: flex; align-items: center; justify-content: flex-end; gap: 8px; line-height: 1.75; }
  .contact-list svg { width: 15px; height: 15px; }
</style>
</head>
<body>
<main class="canvas">
  <section class="card card-front">
    <div class="brand-name">Bright Oak Fitness</div>
    <p class="tagline">“More Than A Gym”</p>
  </section>

  <section class="card card-back">
    <svg class="back-shapes" viewBox="0 0 700 400" aria-hidden="true">
      <polygon points="0,180 255,180 330,400 0,400" fill="var(--ink-black)"/>
      <polygon points="385,250 700,250 700,400 440,400" fill="var(--ink-black)"/>
    </svg>
    <div class="brand-name">Bright Oak Fitness</div>
    <ul class="social-list">
      <li class="social-item"><span class="social-dot"></span>@brightoakfitness</li>
      <li class="social-item"><span class="social-dot"></span>@brightoakfitness</li>
      <li class="social-item"><span class="social-dot"></span>@brightoakfitness</li>
    </ul>
    <div class="person">
      <div class="person-name">Your Name</div>
      <div class="person-title">TITLE</div>
      <div>2817 Mossgrove Bend Road</div>
      <div>Tavares, Florida 32190</div>
    </div>
    <ul class="contact-list">
      <li>352-555-Jump (5867)
        <svg viewBox="0 0 16 16"><circle cx="8" cy="8" r="7" fill="none" stroke="#fff" stroke-width="1.3"/><path d="M5.5 4.5l1.5 0 0.8 2-1 0.8a5 5 0 0 0 2 2l0.8-1 2 0.8v1.5c-3.5 0.3-6.4-2.6-6.1-6.1z" fill="#fff"/></svg></li>
      <li>info@brightoakfitness.example
        <svg viewBox="0 0 16 16"><rect x="2" y="4" width="12" height="8" fill="none" stroke="#fff" stroke-width="1.3"/><path d="M2 4l6 5 6-5" fill="none" stroke="#fff" stroke-width="1.3"/></svg></li>
      <li>www.brightoakfitness.example
        <svg viewBox="0 0 16 16"><circle cx="8" cy="8" r="6.5" fill="none" stroke="#fff" stroke-width="1.3"/><ellipse cx="8" cy="8" rx="2.8" ry="6.5" fill="none" stroke="#fff" stroke-width="1.1"/><path d="M1.5 8h13" stroke="#fff" stroke-width="1.1"/></svg></li>
    </ul>
  </section>
</main>
</body>
</html>
```